Aspiring new agent needs for sale signs for real estate :D

I need a for sale sign that is branding myself as I will be a solo agent here soon. If I like it, I will also decides to get business cards made as well as other images for my business. I want to keep it all cohesive and similar so my branding doesn't jump around.

I'm looking for a design that I can have printed as a for sale sigh on my real estate listings. Must say FOR SALE at the top. Be a vertically oriented rectangle, have Mina Todrow Realtor 555-418-7731 on it. It will also need space saved for the Harlow Penfield logo at the bottom and disclosure on it but I will provide that once I've found the design I'm in favor of. I like light colors, but because of the brokerage I'm in, it needs some red in the design. I also want the picture of myself provided on the design. Thank you :)

Industry/Entity Type

Real Estate Agent

Logo Text

Mina Todrow Real estate 555-418-7730 HP Northreach Group, Harlow Penfield Realty, Each office is independently owned and operated

Logo styles of interest
Abstract Logo
Wordmark Logo
Requirements
Must have
• For Sale sign posted at top. Mina Todrow Realtor. The picture I provided. I also need red in there as the brokerage I work for uses those colors. I like light colors as well, and white.

```html
<!DOCTYPE html>
<html lang="en">
<head>
<meta charset="utf-8">
<title>For Sale Sign – Mina Todrow</title>
<link href="https://fonts.googleapis.com/css2?family=Montserrat:wght@600;700&family=Open+Sans:wght@600&family=Roboto+Condensed:wght@400&display=swap" rel="stylesheet">
<style>
  :root {
    --brand-red: #d3273a;
    --ink-black: #000000;
    --paper: #ffffff;
    --stage: #e2e2e2;
    --muted-gray: #6b6b6b;
    --photo-green: #8f9a72;
    --photo-hair: #5a3f2e;
    --photo-pink: #ecd3d3;
  }
  * { margin: 0; padding: 0; box-sizing: border-box; }
  html, body {
    width: 1200px; height: 960px; overflow: hidden;
    background: var(--stage);
  }
  .sign {
    position: absolute;
    left: 262px; top: 30px;
    width: 675px; height: 900px;
    background: var(--paper);
    display: flex; flex-direction: column;
  }
  .sign__headline {
    height: 168px;
    background: var(--brand-red);
    color: var(--paper);
    font-family: "Montserrat", sans-serif;
    font-weight: 700;
    font-size: 120px;
    letter-spacing: -1px;
    display: flex; align-items: center; justify-content: center;
    line-height: 1;
  }
  .sign__agent {
    position: relative;
    height: 532px;
  }
  .agent-photo {
    position: absolute; inset: 0;
    clip-path: polygon(394px 0, 675px 0, 675px 100%, 352px 100%);
    background:
      radial-gradient(ellipse 120px 150px at 540px 250px, #e8c2ad 0%, rgba(232,194,173,0) 100%),
      radial-gradient(ellipse 200px 240px at 540px 330px, var(--photo-hair) 0%, rgba(90,63,46,0) 100%),
      linear-gradient(180deg, var(--photo-green) 0%, #b8bda3 45%, var(--photo-pink) 100%);
  }
  .agent-name {
    position: absolute;
    left: 16px; top: 158px;
    color: var(--brand-red);
    font-family: "Montserrat", sans-serif;
    font-weight: 700;
    font-size: 78px;
    line-height: 0.98;
    letter-spacing: -1px;
  }
  .agent-title {
    position: absolute;
    left: 22px; top: 318px;
    color: var(--muted-gray);
    font-family: "Roboto Condensed", sans-serif;
    font-size: 46px;
    line-height: 1;
  }
  .sign__phone {
    height: 106px;
    background: var(--ink-black);
    color: var(--paper);
    font-family: "Open Sans", sans-serif;
    font-weight: 600;
    font-size: 88px;
    letter-spacing: 3px;
    display: flex; align-items: center; justify-content: center;
    line-height: 1;
  }
  .sign__brokerage {
    flex: 1;
    padding: 16px 0 0 16px;
    color: var(--muted-gray);
    font-family: "Montserrat", sans-serif;
  }
  .brokerage-team {
    font-weight: 700;
    font-size: 30px; line-height: 1;
    color: var(--brand-red);
  }
  .brokerage-name {
    margin-top: 8px;
    font-weight: 600;
    font-size: 15px; line-height: 1;
    text-transform: uppercase;
  }
  .brokerage-disclosure {
    margin-top: 4px;
    font-weight: 600;
    font-size: 9px; line-height: 1;
  }
</style>
</head>
<body>
  <main class="sign">
    <header class="sign__headline">FOR SALE</header>
    <section class="sign__agent">
      <div class="agent-photo" role="img" aria-label="Portrait photo of the agent, smiling, long dark wavy hair, pink top, outdoor background"></div>
      <h1 class="agent-name">MINA<br>TODROW</h1>
      <p class="agent-title">Realtor®</p>
    </section>
    <div class="sign__phone">555-418-7730</div>
    <footer class="sign__brokerage">
      <div class="brokerage-team">HP Northreach Group</div>
      <div class="brokerage-name">Harlow Penfield Realty</div>
      <div class="brokerage-disclosure">Each office is independently owned and operated</div>
    </footer>
  </main>
</body>
</html>
```